Beer Label

We need a design for our new beer label. It needs to be slick, but there is one little catch. The logo of the brand was made by the client, and in our humble opinion it is not very esthetic.

The bottle is ambar dark so we need to be smart with the colors. The beer is made essentially from HONEY (its a HONEY LAGER).

So attached is the logo of the brand, we need to have in the design the regular information of a beer:

"Producida y Embasada en Republica Dominicana"
"4% alcohol"

Font styles to use
Script

Requirements
Must have
• There must be the regular label and the small one on the neck of the bottle that matches the design.

```html
<!DOCTYPE html>
<html lang="es">
<head>
<meta charset="utf-8">
<title>Campo Dorado Honey Lager – Label</title>
<link href="https://fonts.googleapis.com/css2?family=Cinzel:wght@700&family=Pinyon+Script&display=swap" rel="stylesheet">
<style>
  :root {
    --bg-light: #f6e6c4;
    --bg-mid: #d9a965;
    --bg-dark: #bd8746;
    --label-green: #1d6a2a;
    --label-green-dark: #0f3f17;
    --paper: #d8c9a8;
    --paper-dark: #a8977a;
    --oval-light: #9a8a6e;
    --oval-dark: #4d4231;
    --gold: #e2b45a;
    --cream: #efe3c6;
    --emblem: #7f9a55;
    --wreath: #a89570;
  }
  html, body {
    margin: 0;
    width: 848px;
    height: 1200px;
    overflow: hidden;
  }
  .canvas {
    position: relative;
    width: 848px;
    height: 1200px;
    background: radial-gradient(ellipse 60% 50% at 50% 52%, var(--bg-light) 0%, var(--bg-mid) 55%, var(--bg-dark) 100%);
  }
  .label-art {
    position: absolute;
    left: 0;
    top: 0;
  }
  .brand-name {
    font-family: "Cinzel", serif;
    font-weight: 700;
    fill: var(--cream);
  }
  .product-title {
    font-family: "Cinzel", serif;
    font-weight: 700;
    fill: var(--gold);
  }
  .since-line {
    font-family: "Cinzel", serif;
    font-weight: 700;
    fill: var(--cream);
    letter-spacing: 1px;
  }
  .origin-line,
  .spec-line {
    font-family: "Pinyon Script", cursive;
    fill: var(--cream);
  }
</style>
</head>
<body>
<main class="canvas">
  <svg class="label-art" width="848" height="1200" viewBox="0 0 848 1200" xmlns="http://www.w3.org/2000/svg">
    <defs>
      <linearGradient id="ovalFill" x1="0" y1="0" x2="1" y2="1">
        <stop offset="0" stop-color="var(--oval-light)"/>
        <stop offset="0.5" stop-color="#6e604a"/>
        <stop offset="1" stop-color="var(--oval-dark)"/>
      </linearGradient>
      <linearGradient id="paperFill" x1="0" y1="0" x2="0" y2="1">
        <stop offset="0" stop-color="var(--paper)"/>
        <stop offset="1" stop-color="var(--paper-dark)"/>
      </linearGradient>
      <linearGradient id="neckBand" x1="0" y1="0" x2="0" y2="1">
        <stop offset="0" stop-color="#3c4a22"/>
        <stop offset="1" stop-color="#1f2a10"/>
      </linearGradient>
    </defs>

    <g class="neck-label">
      <rect class="neck-band" x="370" y="365" width="108" height="92" fill="url(#neckBand)"/>
      <ellipse class="neck-oval-frame" cx="424" cy="405" rx="48" ry="68" fill="var(--label-green-dark)"/>
      <ellipse class="neck-oval" cx="424" cy="405" rx="43" ry="63" fill="var(--label-green)"/>
      <ellipse class="neck-emblem-area" cx="424" cy="385" rx="28" ry="30" fill="var(--emblem)" role="img" aria-label="Brand emblem scene: flowers over green fields"/>
      <text class="brand-name" x="424" y="429" font-size="9" text-anchor="middle">Campo Dorado</text>
      <text class="since-line" x="424" y="445" font-size="6" text-anchor="middle">HONEY LAGER</text>
    </g>

    <g class="main-label">
      <rect class="paper-band" x="333" y="702" width="196" height="180" fill="url(#paperFill)"/>
      <ellipse class="oval-frame" cx="428" cy="790" rx="84" ry="130" fill="var(--label-green-dark)"/>
      <ellipse class="oval-border" cx="428" cy="790" rx="80" ry="126" fill="var(--label-green)"/>
      <ellipse class="oval-field" cx="428" cy="790" rx="74" ry="120" fill="url(#ovalFill)"/>

      <rect class="wreath-top-left" x="376" y="700" width="24" height="14" rx="7" fill="var(--wreath)" opacity="0.7" role="img" aria-label="Laurel wreath ornament, left"/>
      <rect class="wreath-top-right" x="456" y="700" width="24" height="14" rx="7" fill="var(--wreath)" opacity="0.7" role="img" aria-label="Laurel wreath ornament, right"/>
      <rect class="emblem-area" x="404" y="684" width="48" height="50" rx="6" fill="var(--emblem)" role="img" aria-label="Brand emblem scene: flowers over green fields"/>
      <text class="brand-name" x="428" y="750" font-size="10" text-anchor="middle">Campo Dorado</text>

      <text class="product-title" x="428" y="790" font-size="36" text-anchor="middle">HONEY</text>
      <text class="since-line" x="428" y="806" font-size="8" text-anchor="middle">SINCE 1989</text>
      <text class="product-title" x="428" y="838" font-size="36" text-anchor="middle">LAGER</text>

      <text class="origin-line" x="428" y="858" font-size="12" text-anchor="middle">Producida y Embasada en</text>
      <text class="origin-line" x="428" y="871" font-size="12" text-anchor="middle">Republica Dominicana</text>

      <text class="spec-line" x="406" y="886" font-size="8" text-anchor="middle">4% Alcohol</text>
      <text class="spec-line" x="452" y="886" font-size="8" text-anchor="middle">355 Ml</text>

      <rect class="wreath-bottom" x="400" y="892" width="56" height="12" rx="6" fill="var(--wreath)" opacity="0.7" role="img" aria-label="Laurel wreath ornament"/>
    </g>
  </svg>
</main>
</body>
</html>
```